Postcard to market investment strategy

Harborline Capital Partners (HCP) has offered investment solutions for over 30 years and we would like to highlight one of our Separately Managed Accounts (SMA) strategies. The strategy is called “Steady Harvest” and is an income focused strategy with a track record exceeding 5 years. The strategy invests in a basket of Closed End Funds that are currently selling at attractive discounts, pay a high dividend and based on our outlook offer net asset value appreciation potential. This strategy has a strong track record and key points to consider include:
1. Top Ranked Strategy
2. Above Average Income
3. Available in both SMA and UMA
4. Minimums as low as $50,000
5. Current Income around 6% to 7%
6. Outpaced the Q&R 700 since inception

Industry/Entity Type

Investment

```html
<!DOCTYPE html>
<html lang="en">
<head>
<meta charset="utf-8">
<title>Harborline Capital Partners – Steady Harvest Postcard</title>
<link rel="stylesheet" href="https://fonts.googleapis.com/css2?family=Arimo:wght@400;700&display=swap">
<style>
  :root{
    --page:#ecebe7;
    --blue:#2f5aa8;
    --navy:#1d3b78;
    --sky-top:#9cc4ea;
    --sky-mid:#d8e9f7;
    --grass:#7fb043;
    --grass-light:#b7d77a;
    --orange:#e07a2c;
    --ink:#2b3a55;
    --line:#9aa7bd;
    --white:#ffffff;
  }
  *{box-sizing:border-box;margin:0;padding:0}
  html,body{width:1200px;height:1000px;overflow:hidden}
  body{background:var(--page);font-family:"Arimo",Arial,sans-serif;color:var(--ink);position:relative}

  .postcard{position:absolute;left:262px;width:676px;height:450px;background:var(--white);overflow:hidden;box-shadow:0 6px 18px rgba(0,0,0,.18)}
  .postcard--front{top:30px}
  .postcard--back{top:520px}

  .top-band{position:absolute;left:0;top:0;width:100%;height:20px;background:var(--blue)}
  .contact-band{position:absolute;left:0;bottom:0;height:44px;background:var(--orange);display:flex;align-items:center;color:var(--white);font-weight:700}

  /* brand name: invented name set plainly in the text font */
  .brand-name{display:block;font-weight:400;color:var(--navy);line-height:1.15}

  /* front */
  .front-backdrop{position:absolute;left:0;top:20px;width:100%;height:386px;background:linear-gradient(180deg,var(--sky-mid) 0%,#f3f8fc 55%,#eaf3dc 80%,var(--grass-light) 100%)}
  .front-photo{position:absolute;right:0;top:20px;width:400px;height:386px;background:linear-gradient(180deg,var(--sky-top) 0%,var(--sky-mid) 50%,var(--grass-light) 75%,var(--grass) 100%)}
  .front-content{position:absolute;left:28px;top:52px;width:310px}
  .front-content .brand-name{font-size:26px}
  .intro{font-size:8.5px;line-height:1.45;margin-top:20px}
  .intro strong{color:var(--orange);text-transform:uppercase}
  .key-points{list-style:none;margin-top:12px}
  .key-points li{display:flex;align-items:center;gap:8px;font-size:13.5px;font-weight:700;color:var(--navy);margin-bottom:5px;white-space:nowrap}
  .key-points svg{flex:none}
  .postcard--front .contact-band{width:100%;justify-content:space-around;font-size:13px;padding:0 10px}
  .contact-item{display:flex;align-items:center;gap:6px;white-space:nowrap}

  /* back */
  .back-panel{position:absolute;left:0;top:20px;width:392px;height:430px;background:linear-gradient(180deg,var(--sky-mid) 0%,#f1f7fc 55%,#e4f0d2 78%,var(--grass) 100%)}
  .back-content{position:absolute;left:24px;top:40px;width:350px}
  .about{font-size:8.5px;line-height:1.5}
  .about strong{color:var(--navy)}
  .sub-head{color:var(--orange);font-weight:700;font-size:10.5px;margin:12px 0 5px}
  .values{list-style:none;font-size:8.5px;line-height:1.5}
  .values li::before{content:"- "}
  .engaged{color:var(--orange);font-weight:700;font-size:10.5px;margin-top:10px}
  .back-content .brand-name{font-size:20px;margin-top:20px}
  .postcard--back .contact-band{width:392px;padding-left:24px;font-size:13px;white-space:nowrap}

  .mail-side{position:absolute;left:392px;top:0;width:284px;height:450px;background:var(--white)}
  .postage-area{position:absolute;right:18px;top:30px;width:70px;height:56px;border:1px solid var(--line);font-size:10px;text-align:center;padding-top:14px;color:var(--ink)}
  .address-area{position:absolute;left:40px;top:150px;width:200px;color:var(--ink)}
  .address-area h3{font-size:12px;font-weight:400;text-align:center;margin-bottom:18px}
  .address-area p{font-size:7.5px;line-height:1.4}
  .barcode-area{position:absolute;left:40px;bottom:60px;width:200px;text-align:center;font-size:11px;color:var(--ink)}
</style>
</head>
<body>

<section class="postcard postcard--front" aria-label="Postcard front">
  <div class="front-backdrop"></div>
  <div class="front-photo" role="img" aria-label="Photo: person in blue shirt with briefcase leaping over a grassy meadow under a bright blue sky"></div>
  <div class="top-band"></div>

  <div class="front-content">
    <span class="brand-name">Harborline Capital Partners</span>

    <p class="intro"><strong>Steady Harvest</strong> is an income focused strategy with a track record exceeding 5 years. The strategy invests in a basket of Closed End Funds currently selling at attractive discounts, pays a high dividend and, based on our outlook, offers net asset value appreciation potential. This strategy has a strong track record and key points to consider include:</p>

    <ul class="key-points">
      <li><svg width="12" height="12" viewBox="0 0 12 12"><path d="M1 6l3 3 7-8" fill="none" stroke="#e07a2c" stroke-width="2.4"/></svg>Top Ranked Strategy</li>
      <li><svg width="12" height="12" viewBox="0 0 12 12"><path d="M1 6l3 3 7-8" fill="none" stroke="#e07a2c" stroke-width="2.4"/></svg>Above Average Income</li>
      <li><svg width="12" height="12" viewBox="0 0 12 12"><path d="M1 6l3 3 7-8" fill="none" stroke="#e07a2c" stroke-width="2.4"/></svg>Available in both SMA and UMA</li>
      <li><svg width="12" height="12" viewBox="0 0 12 12"><path d="M1 6l3 3 7-8" fill="none" stroke="#e07a2c" stroke-width="2.4"/></svg>Minimums as low as $50,000</li>
      <li><svg width="12" height="12" viewBox="0 0 12 12"><path d="M1 6l3 3 7-8" fill="none" stroke="#e07a2c" stroke-width="2.4"/></svg>Current Income around 6% to 7%</li>
      <li><svg width="12" height="12" viewBox="0 0 12 12"><path d="M1 6l3 3 7-8" fill="none" stroke="#e07a2c" stroke-width="2.4"/></svg>Outpaced the Q&amp;R 700 since inception</li>
    </ul>
  </div>

  <div class="contact-band">
    <span class="contact-item"><svg width="14" height="14" viewBox="0 0 24 24"><path d="M6.6 10.8a15 15 0 006.6 6.6l2.2-2.2c.3-.3.7-.4 1-.2 1.1.4 2.3.6 3.6.6.6 0 1 .4 1 1V20c0 .6-.4 1-1 1A17 17 0 013 4c0-.6.4-1 1-1h3.5c.6 0 1 .4 1 1 0 1.3.2 2.5.6 3.6.1.3 0 .7-.2 1z" fill="#fff"/></svg>888.555.0142</span>
    <span class="contact-item"><svg width="14" height="14" viewBox="0 0 24 24"><circle cx="12" cy="12" r="10" fill="none" stroke="#fff" stroke-width="2"/><path d="M2 12h20M12 2c3 3 3 17 0 20M12 2c-3 3-3 17 0 20" fill="none" stroke="#fff" stroke-width="1.5"/></svg>www.harborlinecapital.example</span>
    <span class="contact-item"><svg width="14" height="14" viewBox="0 0 24 24"><rect x="2" y="5" width="20" height="14" fill="none" stroke="#fff" stroke-width="2"/><path d="M2 5l10 8 10-8" fill="none" stroke="#fff" stroke-width="2"/></svg>service@harborlinecapital.example</span>
  </div>
</section>

<section class="postcard postcard--back" aria-label="Postcard back">
  <div class="back-panel" role="img" aria-label="Soft sky background with light swirls fading into green meadow grass"></div>
  <div class="top-band"></div>

  <div class="back-content">
    <p class="about">Established in 1979, <strong>Harborline Capital Partners, Inc. (HCP)</strong> has been a trusted resource for financial advisors. Our experienced team provides a broad range of carefully selected solutions and ongoing support, along with a lasting commitment to every advisor relationship we build.</p>
    <p class="sub-head">HCP empowers financial professionals to succeed</p>
    <ul class="values">
      <li>We create lasting partnerships built on a foundation of trust.</li>
      <li>We utilize our skills, technology and market insight to provide sound guidance.</li>
      <li>We collaborate with financial professionals to provide thoughtful solutions.</li>
      <li>We have an unwavering commitment to excellence in everything we do.</li>
    </ul>
    <p class="engaged">We're fully engaged in our clients' success</p>
    <span class="brand-name">Harborline Capital Partners</span>
  </div>

  <div class="contact-band">Visit us online: www.harborlinecapital.example</div>

  <div class="mail-side">
    <div class="postage-area">Postage<br>Area</div>
    <div class="address-area">
      <h3>Address Area</h3>
      <p>Only the recipient mailing address may appear in this area. The address block must be kept clear of graphics, tints and any other printed text.</p>
    </div>
    <div class="barcode-area">Barcode Area</div>
  </div>
</section>

</body>
</html>
```